Business Card Design Project for a Restaurant/Wine Bar

New, fresh business card design for Verdano Wine Bar & Restaurant, Alder Cove, Nordland. We are an established restaurant on the Nordland coast featuring "Italian coastal cuisine."

"Verdano" means bay leaf in Italian. We aren't sure if we would like our logo on the card or not, but if you have something interesting that uses it, then please do so. The basic information is essential - full restaurant name, address, phone and website (do not use www). The font on our menu and wine list may give you some sort of an idea of our style.

One-sided card needed as we often use the backside to write down various types of info for customers.

After seeing a few submissions, we would like to see what designers can come up with-using the logo, just the leaf, or none at all. Sky is the limit as long as our full restaurant name, address, phone and website (please leave out www) are there. Please contact us if questions!

I appreciate all of your designs! Our deadline is next week, but I will continue to give feedback on designs as I can. This is our busiest season, so my co-owner/chef/husband, won't have time to look at the designs for awhile. When he does, we can make our decision.

cheers,
Mirel

Target Market(s)

Fine dining/wine crowd. Would like something simple and elegant, but not pretentious or stuffy. Verdano means bay laurel (bay leaf) in Italian (please see our logo).

Industry/Entity Type

Restaurant

Requirements
Must have
• Full Name of Restaurant: Verdano Wine Bar & Restaurant
Address: 812 Fenwick Ave NW, Alder Cove, Nordland 97538
Phone: 541.555.0193
website: verdanowinebar.example (do not use www)
Should not have
• Loud colors.

```html
<!DOCTYPE html>
<html lang="en">
<head>
<meta charset="utf-8">
<title>Verdano Wine Bar &amp; Restaurant — Business Card</title>
<link rel="stylesheet" href="https://fonts.googleapis.com/css2?family=IM+Fell+English+SC&display=swap">
<style>
  :root {
    --card-black: #0c0b0a;
    --card-yellow: #f4d82c;
    --ink: #17120a;
    --leaf-gold: #a8821c;
    --leaf-deep: #6e5410;
    --type: "IM Fell English SC", "Times New Roman", serif;
  }
  html, body {
    margin: 0;
    padding: 0;
    width: 1200px;
    height: 727px;
    overflow: hidden;
    background: var(--card-black);
  }
  .card {
    position: relative;
    width: 1200px;
    height: 727px;
    background: var(--card-black);
    font-family: var(--type);
    color: var(--ink);
  }
  .card__website {
    position: absolute;
    top: 15px;
    left: 0;
    width: 1200px;
    text-align: center;
    font-size: 19px;
    line-height: 1;
    letter-spacing: 1px;
    color: var(--card-yellow);
  }
  .card__panel {
    position: absolute;
    left: 46px;
    top: 46px;
    width: 1108px;
    height: 621px;
    background: var(--card-yellow);
    overflow: hidden;
  }
  .card__foliage {
    position: absolute;
    right: 0;
    top: 0;
    width: 560px;
    height: 480px;
    background: radial-gradient(closest-side at 65% 38%, rgba(110, 84, 16, 0.75) 0%, rgba(168, 130, 28, 0.55) 50%, rgba(244, 216, 44, 0) 100%);
  }
  .card__name {
    position: absolute;
    left: 32px;
    top: 196px;
    margin: 0;
    font-size: 118px;
    font-weight: 400;
    line-height: 1;
    letter-spacing: 2px;
    color: var(--ink);
  }
  .card__tagline {
    position: absolute;
    left: 49px;
    top: 320px;
    margin: 0;
    font-size: 47px;
    font-weight: 400;
    line-height: 1;
    letter-spacing: 1px;
    color: var(--ink);
  }
  .card__address {
    position: absolute;
    left: 0;
    width: 1108px;
    top: 588px;
    margin: 0;
    text-align: center;
    font-size: 27px;
    line-height: 1;
    letter-spacing: 1.5px;
    color: var(--ink);
  }
  .card__rule {
    position: absolute;
    left: 46px;
    top: 678px;
    width: 1108px;
    height: 2px;
    background: var(--card-yellow);
  }
  .card__phone {
    position: absolute;
    left: 0;
    width: 1200px;
    top: 684px;
    text-align: center;
    font-size: 32px;
    line-height: 1;
    letter-spacing: 1.5px;
    color: var(--card-yellow);
  }
</style>
</head>
<body>
  <div class="card">
    <div class="card__website">VERDANOWINEBAR.EXAMPLE</div>
    <div class="card__panel">
      <div class="card__foliage" role="img" aria-label="Illustrated bay laurel branch with golden leaves reaching in from the top right corner"></div>
      <h1 class="card__name">Verdano</h1>
      <p class="card__tagline">Wine Bar &amp; Restaurant</p>
      <p class="card__address">812 Fenwick Ave NW, Alder Cove, Nordland 97538</p>
    </div>
    <div class="card__rule"></div>
    <div class="card__phone">Phone 541.555.0193</div>
  </div>
</body>
</html>
```